Bref créative
business card and letter head
TCW Roofing & Decks, LLC
Corporate
Dale Harrington
Project Manager / Estimator
7426-B Ferncliff
Houston, TX 77094
daleh4182@quorvix.com
Logo for TCW Roofing & Decks, LLC

```html
<!DOCTYPE html>
<html lang="en">
<head>
<meta charset="utf-8">
<title>TCW Roofing &amp; Decks, LLC — Business Card</title>
<link href="https://fonts.googleapis.com/css2?family=Tinos:wght@400;700&display=swap" rel="stylesheet">
<style>
  :root {
    --navy: #173a66;
    --paper: #ffffff;
    --backdrop: #e9e6e1;
    --card-shadow: rgba(40, 30, 20, 0.18);
  }
  * { margin: 0; padding: 0; box-sizing: border-box; }
  html, body { width: 1200px; height: 871px; overflow: hidden; }
  body {
    background: var(--backdrop);
    font-family: "Tinos", "Times New Roman", serif;
    position: relative;
  }
  .card {
    position: absolute;
    left: 250px;
    width: 700px;
    height: 400px;
    background: var(--paper);
    box-shadow: 0 6px 18px var(--card-shadow);
    overflow: hidden;
  }
  .card--back { top: 20px; }
  .card--front { top: 451px; }

  .wordmark {
    color: var(--navy);
    font-weight: 700;
    line-height: 1;
  }
  .wordmark__initials { display: block; font-size: 92px; letter-spacing: 2px; }
  .wordmark__rest { display: block; font-size: 22px; margin-top: 4px; }

  .card--back .wordmark {
    position: absolute;
    left: 0; right: 0; top: 130px;
    text-align: center;
  }

  .front__panel {
    position: absolute;
    left: 0; top: 0;
    width: 418px; height: 100%;
    background: var(--navy);
    color: var(--paper);
    padding: 30px 0 0 44px;
  }
  .front__rule {
    position: absolute;
    left: 430px; top: 0;
    width: 12px; height: 100%;
    background: var(--navy);
  }
  .front__logo {
    position: absolute;
    left: 442px; right: 0; top: 140px;
    text-align: center;
  }
  .front__logo .wordmark__initials { font-size: 78px; }
  .front__logo .wordmark__rest { font-size: 19px; }

  .person__name { font-size: 22px; }
  .person__title { font-size: 19px; margin-top: 2px; }
  .address { font-size: 20px; margin-top: 48px; line-height: 1.3; }
  .contacts { list-style: none; margin-top: 48px; font-size: 19px; line-height: 1.38; }
  .contacts li { display: flex; align-items: center; gap: 8px; }
  .contacts svg { width: 14px; height: 14px; fill: var(--paper); flex: none; }
</style>
</head>
<body>
  <section class="card card--back" aria-label="Business card back">
    <div class="wordmark">
      <span class="wordmark__initials">TCW</span>
      <span class="wordmark__rest">Roofing &amp; Decks, LLC</span>
    </div>
  </section>

  <section class="card card--front" aria-label="Business card front">
    <div class="front__panel">
      <p class="person__name">Dale Harrington</p>
      <p class="person__title">Project Manager / Estimator</p>
      <p class="address">7426-B Ferncliff<br>Houston, TX 77094</p>
      <ul class="contacts">
        <li><svg viewBox="0 0 16 16" aria-hidden="true"><path d="M3 1h3l1 4-2 1a9 9 0 0 0 5 5l1-2 4 1v3c0 1-1 2-2 2A13 13 0 0 1 1 3c0-1 1-2 2-2z"/></svg>713-555-0142</li>
        <li><svg viewBox="0 0 16 16" aria-hidden="true"><rect x="4" y="0" width="8" height="16" rx="1.5"/><rect x="5.5" y="2" width="5" height="9" fill="#173a66"/></svg>713-555-0187</li>
        <li><svg viewBox="0 0 16 16" aria-hidden="true"><rect x="1" y="6" width="14" height="8" rx="1"/><rect x="4" y="1" width="8" height="5"/></svg>832-555-0163</li>
        <li><svg viewBox="0 0 16 16" aria-hidden="true"><rect x="1" y="3" width="14" height="10" rx="1"/><path d="M1.5 3.5 8 9l6.5-5.5" stroke="#173a66" stroke-width="1.4" fill="none"/></svg>daleh4182@quorvix.com</li>
      </ul>
    </div>
    <div class="front__rule"></div>
    <div class="front__logo wordmark">
      <span class="wordmark__initials">TCW</span>
      <span class="wordmark__rest">Roofing &amp; Decks, LLC</span>
    </div>
  </section>
</body>
</html>
```